I need a 2 Sided Product Line Card for my company Q-Span Corporation. We represent and distribute products for manufacturers of Non-Destructive and Metallurgical Testing Equipment. Our company logo colors are Navy Blue and Black. Any other information needed should be provided in the uploaded files. I provided a copy of our old line card and information needed for new 2022 line card.

```html
<!DOCTYPE html>
<html lang="en">
<head>
<meta charset="utf-8">
<title>Q-Span Corporation – 2022 Line Card</title>
<link href="https://fonts.googleapis.com/css2?family=Montserrat:wght@300;400;500;600;700;800&display=swap" rel="stylesheet">
<style>
  :root{
    --navy:#1f4e98;
    --navy-deep:#1a4a8c;
    --ink:#1d1d1f;
    --text:#333438;
    --panel:#ebebec;
    --white:#ffffff;
    --rule:#c9c9cc;
    --backdrop:#f1f1f2;
  }
  *{box-sizing:border-box;margin:0;padding:0}
  html,body{width:783px;height:1200px;overflow:hidden;background:var(--backdrop)}
  body{position:relative;font-family:'Montserrat',sans-serif;color:var(--text)}

  .slot{position:absolute;top:324px;width:360px;height:552px;box-shadow:0 4px 14px rgba(0,0,0,.18);overflow:hidden;background:var(--white)}
  .slot.front{left:21px}
  .slot.back{left:402px}
  .sheet{position:absolute;left:0;top:0;width:783px;height:1200px;background:var(--white);overflow:hidden;transform:scale(.46);transform-origin:0 0}
  .abs{position:absolute}

  /* front side */
  .brand{left:42px;top:36px;color:var(--navy);font-weight:500;line-height:1}
  .brand .name{font-size:50px;letter-spacing:1px}
  .brand .sub{font-size:17px;letter-spacing:6.5px;margin-top:4px}
  .title{left:320px;top:38px;font-size:49px;font-weight:800;color:var(--navy);letter-spacing:.5px}
  .subtitle{left:322px;top:100px;font-size:13.5px;font-weight:700;color:var(--ink);letter-spacing:.3px}
  .title-rule{left:322px;top:121px;width:456px;height:1px;background:var(--rule)}
  .title-bar{left:362px;top:119px;width:48px;height:6px;border-radius:3px;background:var(--navy)}
  .panel{left:300px;top:155px;width:483px;height:725px;background:var(--panel)}
  .side{left:0;top:155px;width:293px;height:725px}
  .side-head{left:46px;top:262px;color:var(--white);font-size:24px;font-weight:800;line-height:31px;letter-spacing:-.3px}
  .address{left:48px;top:428px;color:var(--white);font-size:18px;font-weight:300;line-height:22px;font-style:normal}
  .contact{left:48px;display:flex;align-items:center;gap:14px;color:var(--white);font-size:13.5px;font-weight:700}
  .contact svg{width:22px;height:22px;flex:none}
  .device{left:52px;top:752px;width:200px;height:78px;border-radius:14px;
    background:linear-gradient(90deg,#4a4450 0%,#3b3840 45%,#f2b21c 46%,#f5a80f 100%)}
  .forklift{left:540px;top:610px;width:243px;height:245px;border-radius:6px;
    background:linear-gradient(160deg,#d9d9db 0%,#8f9093 40%,#f1b81d 62%,#3a3a3c 100%);opacity:.85}
  .products{left:333px;top:190px;list-style:none}
  .products li{display:flex;align-items:center;gap:18px;height:37.6px;font-size:14.5px;color:var(--text)}
  .products svg{width:16px;height:16px;flex:none}
  .banner{left:62px;top:856px;width:640px;height:54px}
  .banner-text{left:0;width:783px;top:872px;text-align:center;color:var(--white);font-size:18px;font-weight:700;letter-spacing:.4px}
  .divider{border-left:1.5px dashed #8a8a8e}
  .front .divider{top:947px;height:196px}
  .maker{top:950px}
  .maker .logo{height:80px;display:flex;align-items:center;justify-content:center;color:var(--navy);font-weight:700;font-size:20px;text-align:center;line-height:1.1}
  .maker .label{font-size:12.5px;font-weight:700;color:var(--ink);margin-bottom:10px}
  .maker ul{list-style:none}
  .maker li{display:flex;gap:8px;font-size:11.5px;line-height:14px;margin-bottom:13px;color:var(--text)}
  .maker li svg{width:11px;height:11px;flex:none;margin-top:2px}
  .site{left:0;width:783px;text-align:center;font-size:18px;font-weight:700;letter-spacing:4px;color:var(--ink)}
  .base{left:0;bottom:0;width:783px;height:8px;background:var(--navy)}

  /* back side */
  .back-brand{left:0;width:783px;top:34px;text-align:center;color:var(--navy);font-weight:500;line-height:1}
  .back-brand .name{font-size:54px;letter-spacing:1px}
  .back-brand .sub{font-size:19px;letter-spacing:7px;margin-top:4px}
  .back-band{left:0;top:136px;width:783px;height:122px;background:var(--navy);color:var(--white);text-align:center}
  .back-band h1{font-size:52px;font-weight:800;letter-spacing:1px;margin-top:16px;line-height:1}
  .back-band p{font-size:19px;font-weight:700;letter-spacing:.4px;margin-top:14px}
  .grid{left:44px;top:288px;width:710px;height:790px;display:grid;grid-template-columns:248px 240px 222px;grid-template-rows:repeat(6,1fr)}
  .brand-cell{padding-right:12px}
  .brand-cell:nth-child(3n+2),.brand-cell:nth-child(3n){padding-left:22px}
  .brand-head{display:flex;align-items:center;gap:10px;min-height:42px}
  .brand-head .mark{font-size:18px;font-weight:700;color:var(--navy);line-height:1.05}
  .brand-head .who{font-size:11.5px;font-weight:700;color:var(--ink);line-height:1.2}
  .brand-cell ul{list-style:none;margin-top:10px}
  .brand-cell li{display:flex;gap:7px;font-size:10.5px;line-height:12.5px;color:var(--text)}
  .brand-cell li svg{width:9px;height:9px;flex:none;margin-top:2px}
  .back .divider{top:290px;height:780px}
</style>
</head>
<body>
  <svg width="0" height="0" style="position:absolute">
    <defs>
      <symbol id="tick" viewBox="0 0 16 16">
        <circle cx="8" cy="8" r="8" fill="#1f4e98"/>
        <path d="M4.5 8.3l2.3 2.3 4.7-4.9" fill="none" stroke="#fff" stroke-width="2" stroke-linecap="round" stroke-linejoin="round"/>
      </symbol>
    </defs>
  </svg>

  <!-- Front side -->
  <section class="slot front">
    <div class="sheet">
      <div class="abs brand"><div class="name">Q-SPAN</div><div class="sub">CORPORATION</div></div>
      <h1 class="abs title">2022 LINE CARD</h1>
      <p class="abs subtitle">Q-SPAN COMPANY INFORMATION FOR LINE CARD</p>
      <div class="abs title-rule"></div>
      <div class="abs title-bar"></div>

      <div class="abs panel"></div>
      <svg class="abs side" viewBox="0 0 293 725" preserveAspectRatio="none">
        <polygon points="0,12 156,62 293,0 293,725 0,725" fill="#1a4a8c"/>
      </svg>

      <h2 class="abs side-head">NON-DESTRUCTIVE<br>&amp; MATERIALS<br>TESTING<br>EQUIPMENT</h2>
      <address class="abs address">Q-Span Corporation<br>1820 Harbor Point<br>Dr, #210<br>Westlake Falls,<br>Mi 48000</address>

      <div class="abs contact" style="top:591px">
        <svg viewBox="0 0 22 22"><circle cx="11" cy="11" r="11" fill="#fff"/><path d="M7.5 6.5l2 0 1 2.5-1.2 1a6 6 0 0 0 2.7 2.7l1-1.2 2.5 1v2a1 1 0 0 1-1 1A8.5 8.5 0 0 1 6.5 7.5a1 1 0 0 1 1-1z" fill="#1a4a8c"/></svg>
        555-014-2290
      </div>
      <div class="abs contact" style="top:637px">
        <svg viewBox="0 0 22 22"><circle cx="11" cy="11" r="11" fill="#fff"/><rect x="6" y="7.5" width="10" height="7" rx="1" fill="#1a4a8c"/><path d="M6.5 8l4.5 3.5L15.5 8" fill="none" stroke="#fff" stroke-width="1"/></svg>
        sales@qspancorp.example
      </div>
      <div class="abs contact" style="top:683px">
        <svg viewBox="0 0 22 22"><circle cx="11" cy="11" r="11" fill="#fff"/><g fill="none" stroke="#1a4a8c" stroke-width="1.2"><circle cx="11" cy="11" r="5"/><ellipse cx="11" cy="11" rx="2.2" ry="5"/><path d="M6 11h10"/></g></svg>
        www.qspancorp.example
      </div>

      <div class="abs device" role="img" aria-label="Handheld thermal imaging inspection device"></div>

      <ul class="abs products">
        <li><svg><use href="#tick"/></svg>Eddy Current Flaw &amp; Sorting Systems</li>
        <li><svg><use href="#tick"/></svg>Ultrasonic Flaw &amp; Thickness Gauges</li>
        <li><svg><use href="#tick"/></svg>Magnetic Particle Systems</li>
        <li><svg><use href="#tick"/></svg>Liquid Penetrant Systems</li>
        <li><svg><use href="#tick"/></svg>X-ray Systems</li>
        <li><svg><use href="#tick"/></svg>Leak And Flow Test Systems</li>
        <li><svg><use href="#tick"/></svg>Resonant Frequency Systems</li>
        <li><svg><use href="#tick"/></svg>Acoustic Emission Systems</li>
        <li><svg><use href="#tick"/></svg>Videoscopes, Borescopes, Microscopes</li>
        <li><svg><use href="#tick"/></svg>Vision And Infrared Cameras</li>
        <li><svg><use href="#tick"/></svg>Dimentional Gauging Systems</li>
        <li><svg><use href="#tick"/></svg>Xrf &amp; Libs Analyzers</li>
        <li><svg><use href="#tick"/></svg>Hardness Testers</li>
        <li><svg><use href="#tick"/></svg>Oes Analyzers</li>
        <li><svg><use href="#tick"/></svg>Rental Equipment</li>
        <li><svg><use href="#tick"/></svg>Contract Testing</li>
        <li><svg><use href="#tick"/></svg>Ndt Training Classes</li>
      </ul>

      <div class="abs forklift" role="img" aria-label="Yellow industrial forklift"></div>

      <svg class="abs banner" viewBox="0 0 640 54">
        <path d="M0 0 H640 A20 20 0 0 0 620 20 V30 Q620 54 596 54 H44 Q20 54 20 30 V20 A20 20 0 0 0 0 0Z" fill="#1d1d1f"/>
      </svg>
      <h3 class="abs banner-text">MANUFACTURERS AND PRINCIPALS REPRESENTED</h3>

      <div class="abs divider" style="left:255px"></div>
      <div class="abs divider" style="left:517px"></div>

      <div class="abs maker" style="left:54px;width:190px">
        <div class="logo">Northvale</div>
        <p class="label" style="margin-top:20px">Northvale Material Systems</p>
        <ul>
          <li><svg><use href="#tick"/></svg>Resonant Frequency Technology</li>
          <li><svg><use href="#tick"/></svg>Manual &amp; Automated Solutions</li>
        </ul>
      </div>

      <div class="abs maker" style="left:304px;width:200px">
        <div class="logo">HARLOW &amp; FINCH</div>
        <p class="label" style="margin-top:20px">Harlow &amp; Finch NDE</p>
        <ul>
          <li><svg><use href="#tick"/></svg>UV &amp; WL Meters</li>
          <li><svg><use href="#tick"/></svg>Field Strength Meters</li>
        </ul>
      </div>

      <div class="abs maker" style="left:555px;width:200px">
        <div class="logo" style="height:50px;justify-content:flex-start">Kestrel NDT</div>
        <p class="label" style="margin-top:19px">Kestrel NDT</p>
        <ul>
          <li><svg><use href="#tick"/></svg>Magnetic Particle<br>Benches / Lines</li>
          <li><svg><use href="#tick"/></svg>Liquid Penetrant</li>
          <li><svg><use href="#tick"/></svg>Portable &amp; Overhead<br>Blacklights</li>
        </ul>
      </div>

      <p class="abs site" style="top:1150px">www.qspancorp.example</p>
      <div class="abs base"></div>
    </div>
  </section>

  <!-- Back side -->
  <section class="slot back">
    <div class="sheet">
      <div class="abs back-brand"><div class="name">Q-SPAN</div><div class="sub">CORPORATION</div></div>
      <header class="abs back-band">
        <h1>2022 LINE CARD</h1>
        <p>Q-SPAN COMPANY INFORMATION FOR LINE CARD</p>
      </header>

      <div class="abs divider" style="left:281px"></div>
      <div class="abs divider" style="left:520px"></div>

      <div class="abs grid">
        <div class="brand-cell">
          <div class="brand-head"><span class="mark">DALMOR</span><span class="who">Dalmor Instruments</span></div>
          <ul><li><svg><use href="#tick"/></svg>Hall Effect Thickness Gauges</li><li><svg><use href="#tick"/></svg>Hall Effect Accessories</li></ul>
        </div>
        <div class="brand-cell">
          <div class="brand-head"><span class="mark">Greyfield</span><span class="who">Greyfield<br>Industrial Test</span></div>
          <ul><li><svg><use href="#tick"/></svg>Leak and Flow Testing Systems</li><li><svg><use href="#tick"/></svg>Dimensional Gauging Systems</li><li><svg><use href="#tick"/></svg>Automated Inspection Systems</li></ul>
        </div>
        <div class="brand-cell">
          <div class="brand-head"><span class="mark">provant</span><span class="who">Provant</span></div>
          <ul><li><svg><use href="#tick"/></svg>Portable Leeb Hardness Testers</li><li><svg><use href="#tick"/></svg>Portable UCI Hardness Testers</li><li><svg><use href="#tick"/></svg>Portable Rockwell Hardness Testers</li></ul>
        </div>

        <div class="brand-cell">
          <div class="brand-head"><span class="mark">Delmarsh</span><span class="who">Delmarsh</span></div>
          <ul><li><svg><use href="#tick"/></svg>Coating Thickness Gauges</li><li><svg><use href="#tick"/></svg>Surface Profile Gauges</li><li><svg><use href="#tick"/></svg>Adhesion Testers</li></ul>
        </div>
        <div class="brand-cell">
          <div class="brand-head"><span class="mark">ibex</span><span class="who">Ibex NDT Systems</span></div>
          <ul><li><svg><use href="#tick"/></svg>Crack Detection Instruments</li><li><svg><use href="#tick"/></svg>Material Sorting Instruments</li><li><svg><use href="#tick"/></svg>Multi-Channel Instruments</li><li><svg><use href="#tick"/></svg>Custom Automated Systems</li></ul>
        </div>
        <div class="brand-cell">
          <div class="brand-head"><span class="mark">TONALIS</span><span class="who">Tonalis</span></div>
          <ul><li><svg><use href="#tick"/></svg>Single Channel EMAR Systems</li><li><svg><use href="#tick"/></svg>Multi-Channel EMAR Systems</li><li><svg><use href="#tick"/></svg>EMAT Transducers &amp; Accessories</li></ul>
        </div>

        <div class="brand-cell">
          <div class="brand-head"><span class="mark">RIDGE</span><span class="who">Ridge Ultrasonics</span></div>
          <ul><li><svg><use href="#tick"/></svg>Ambient Temperature Couplants</li><li><svg><use href="#tick"/></svg>High Temperature Couplants</li><li><svg><use href="#tick"/></svg>Fluid Couplants for AUT and<br>Robotic Inspections</li></ul>
        </div>
        <div class="brand-cell">
          <div class="brand-head"><span class="mark">ALLOY</span><span class="who">Alloy Review<br>Group</span></div>
          <ul><li><svg><use href="#tick"/></svg>Portable and Bench XRF Analyzers</li><li><svg><use href="#tick"/></svg>Portable and Bench LIBS Analyzers</li><li><svg><use href="#tick"/></svg>OES Systems</li></ul>
        </div>
        <div class="brand-cell">
          <div class="brand-head"><span class="mark">SIGNAL</span><span class="who">Signal Mesh<br>Networks</span></div>
          <ul><li><svg><use href="#tick"/></svg>Installed Corrosion Monitoring Sensors</li><li><svg><use href="#tick"/></svg>RVI Systems</li><li><svg><use href="#tick"/></svg>Retrieval &amp; Sampling Tools</li></ul>
        </div>

        <div class="brand-cell">
          <div class="brand-head"><span class="mark">ormond</span><span class="who">Ormond</span></div>
          <ul><li><svg><use href="#tick"/></svg>Portable Hardness Testers</li><li><svg><use href="#tick"/></svg>Bench Rockwell and Brinell Testers</li><li><svg><use href="#tick"/></svg>Automated Hardness Systems</li></ul>
        </div>
        <div class="brand-cell">
          <div class="brand-head"><span class="mark">Newfield</span><span class="who">Newfield</span></div>
          <ul><li><svg><use href="#tick"/></svg>Portable Hardness Testers</li><li><svg><use href="#tick"/></svg>Bench Rockwell and Brinell Machines</li><li><svg><use href="#tick"/></svg>Micro Hardness Testing Systems</li><li><svg><use href="#tick"/></svg>Automated Hardness Testing</li></ul>
        </div>
        <div class="brand-cell">
          <div class="brand-head"><span class="mark">varlo</span><span class="who">Varlo Systeme</span></div>
          <ul><li><svg><use href="#tick"/></svg>Acoustic Emission Systems</li><li><svg><use href="#tick"/></svg>Multi-Channel Systems</li><li><svg><use href="#tick"/></svg>Sensors &amp; Accessories</li></ul>
        </div>

        <div class="brand-cell">
          <div class="brand-head"><span class="mark">CORVID</span><span class="who">Corvid NDE</span></div>
          <ul><li><svg><use href="#tick"/></svg>Conductivity Meters</li><li><svg><use href="#tick"/></svg>Conductivity Standards &amp;<br>Accessories</li></ul>
        </div>
        <div class="brand-cell">
          <div class="brand-head"><span class="mark">PINNACLE</span><span class="who">Pinnacle NDT</span></div>
          <ul><li><svg><use href="#tick"/></svg>Phased Array Spotweld Test Systems</li><li><svg><use href="#tick"/></svg>Transducers &amp; Accessories</li></ul>
        </div>
        <div class="brand-cell">
          <div class="brand-head"><span class="mark">Holloway</span><span class="who">Holloway<br>Technologies</span></div>
          <ul><li><svg><use href="#tick"/></svg>Ultrasonic Thickness Gauges</li><li><svg><use href="#tick"/></svg>Ultrasonic Flaw Detectors</li><li><svg><use href="#tick"/></svg>Eddy Current Instruments</li><li><svg><use href="#tick"/></svg>Multi-Channel Systems</li></ul>
        </div>

        <div class="brand-cell">
          <div class="brand-head"><span class="mark">MARROW</span><span class="who">Marrow Bass</span></div>
          <ul><li><svg><use href="#tick"/></svg>Magnetic Particle Benches / Lines</li><li><svg><use href="#tick"/></svg>Liquid Penetrant Lines</li><li><svg><use href="#tick"/></svg>Mobile MPI Units &amp; Accessories</li></ul>
        </div>
        <div class="brand-cell">
          <div class="brand-head"><span class="mark">PALMER</span><span class="who">Palmer Research<br>Corporation</span></div>
          <ul><li><svg><use href="#tick"/></svg>Portable Contour Probes</li><li><svg><use href="#tick"/></svg>Hi-Amp Portables</li><li><svg><use href="#tick"/></svg>Black Lights, Meters &amp; Accessories</li></ul>
        </div>
        <div class="brand-cell">
          <div class="brand-head"><span class="mark">ZENOVA</span><span class="who">Zenova</span></div>
          <ul><li><svg><use href="#tick"/></svg>Phased Array UT Instruments</li><li><svg><use href="#tick"/></svg>Phased Array ET Instruments</li><li><svg><use href="#tick"/></svg>Multi-Channel Systems</li><li><svg><use href="#tick"/></svg>Scanners &amp; Accessories</li></ul>
        </div>
      </div>

      <p class="abs site" style="top:1128px">www.qspancorp.example</p>
      <div class="abs base"></div>
    </div>
  </section>
</body>
</html>
```